48207 Velmora Lane Ad (for Facebook and Instagram)

Ad to run on Social Media (i.e. Facebook, Instagram etc.)
to advertise sale of property.

Target Market(s)

Prospective Buyers

Requirements
Must have
• TEXT
• Presenting
• 48207 Velmora Lane, Brandywine, MD
• Priced to Sell
• 5 Bedroom / 4 Bathroom Colonial with Contemporary Design and Charm
• Over 5,000 sq ft of Spacious Elegance
• Extraordinary Master Bedroom with Spacious Bath
• Modern Open Concept Kitchen
• Natural Oak Floors
• Stainless Steel Appliances
• Granite Counter-Tops
• Exterior with Outdoor Security, Design Lighting and Sprinkler System
• Just 10 Minutes From Corvel Landing
• Call Marcus Pelley, Realtor
• Dunmore Realty Inc.
• Phone (240) 555-0183
• Email - premierhomedesk@quillmail.example

```html
<!DOCTYPE html>
<html lang="en">
<head>
<meta charset="utf-8">
<title>48207 Velmora Lane – Property For Sale</title>
<link rel="stylesheet" href="https://fonts.googleapis.com/css2?family=Montserrat:wght@700;800&family=Roboto:wght@400;500;700&display=swap">
<style>
  :root {
    --page: #e6e6e8;
    --blue-deep: #0a2f8f;
    --blue-mid: #1560c8;
    --blue-light: #3a9be3;
    --white: #ffffff;
    --navy-text: #1f2f6e;
    --house-tone: #c9c2bb;
    --night-tone: #5a3d7a;
    --portrait-tone: #2a2f3c;
  }
  * { margin: 0; padding: 0; box-sizing: border-box; }
  html, body { width: 1200px; height: 435px; overflow: hidden; background: var(--page); }
  .ad {
    position: absolute; left: 0; top: 76px; width: 1200px; height: 283px;
    overflow: hidden; color: var(--white);
    font-family: "Roboto", Arial, sans-serif;
  }
  .ad__art { position: absolute; inset: 0; width: 100%; height: 100%; }
  .portrait { position: absolute; left: 12px; top: 115px; width: 170px; height: 168px; }
  .intro { position: absolute; left: 0; top: 0; width: 560px; }
  .intro > * { position: absolute; white-space: nowrap; }
  .headline {
    font-family: "Montserrat", Arial, sans-serif; font-weight: 800;
    font-size: 33px; left: 56px; top: 30px; letter-spacing: 0.2px;
  }
  .presenting { font-weight: 500; font-size: 16px; left: 217px; top: 65px; }
  .address { font-weight: 400; font-size: 19px; left: 110px; top: 81px; }
  .priced { font-weight: 500; font-size: 16px; left: 225px; top: 111px; }
  .price {
    font-family: "Montserrat", Arial, sans-serif; font-weight: 800;
    font-size: 30px; left: 158px; top: 127px;
  }
  .call { font-weight: 700; font-size: 19px; left: 149px; top: 166px; }
  .agent { font-weight: 400; font-size: 21px; left: 175px; top: 192px; }
  .agent small { font-size: 10px; font-weight: 500; }
  .brokerage { font-weight: 700; font-size: 13px; left: 180px; top: 219px; }
  .email { font-weight: 400; font-size: 12.5px; left: 180px; top: 236px; }

  .brand {
    position: absolute; left: 834px; top: 33px; width: 178px; height: 52px;
    background: var(--white); display: flex; align-items: center; justify-content: center;
    font-weight: 700; font-size: 15px; color: var(--navy-text); letter-spacing: 0.5px;
  }
  .badge {
    position: absolute; left: 1033px; top: 33px; width: 44px; height: 52px;
    background: var(--white); border: 4px solid var(--blue-deep);
  }
  .details { position: absolute; left: 743px; top: 112px; width: 440px; }
  .details__title { font-weight: 500; font-size: 18px; letter-spacing: 0.2px; margin-bottom: 8px; }
  .details__cols { display: flex; gap: 18px; }
  .details__list { list-style: none; width: 202px; }
  .details__list li {
    position: relative; padding-left: 12px; font-size: 10.6px; line-height: 12.6px;
    margin-bottom: 9px;
  }
  .details__list li svg { position: absolute; left: 0; top: 2px; width: 8px; height: 8px; }
</style>
</head>
<body>
<section class="ad">
  <svg class="ad__art" viewBox="0 0 1376 324" preserveAspectRatio="none" aria-hidden="true">
    <defs>
      <radialGradient id="leftGlow" cx="0.45" cy="0.3" r="0.8">
        <stop offset="0" stop-color="#4aa6ec"/>
        <stop offset="0.6" stop-color="#1a63c9"/>
        <stop offset="1" stop-color="#0a2f8f"/>
      </radialGradient>
      <radialGradient id="rightGlow" cx="0.4" cy="0.35" r="0.8">
        <stop offset="0" stop-color="#48a8ec"/>
        <stop offset="0.6" stop-color="#2372d3"/>
        <stop offset="1" stop-color="#0b3497"/>
      </radialGradient>
      <linearGradient id="houseTone" x1="0" y1="0" x2="0" y2="1">
        <stop offset="0" stop-color="#d9d6d3"/>
        <stop offset="0.55" stop-color="#a9826e"/>
        <stop offset="1" stop-color="#eef0f3"/>
      </linearGradient>
      <linearGradient id="nightTone" x1="0" y1="0" x2="1" y2="1">
        <stop offset="0" stop-color="#3b2a63"/>
        <stop offset="0.5" stop-color="#8a4a7e"/>
        <stop offset="1" stop-color="#2a3366"/>
      </linearGradient>
    </defs>
    <rect width="1376" height="324" fill="url(#leftGlow)"/>
    <polygon points="859,0 1376,0 1376,324 759,324" fill="url(#rightGlow)"/>
    <polygon points="564,0 859,0 759,324 459,324" fill="#ffffff"/>
    <polygon points="568,0 845,0 797,158 518,118" fill="url(#houseTone)" role="img" aria-label="Photo of the colonial brick house in snow"/>
    <polygon points="512,132 792,174 746,324 463,324" fill="url(#nightTone)" role="img" aria-label="Night photo of the waterfront with lit Ferris wheel"/>
  </svg>

  <div class="portrait" role="img" aria-label="Portrait of the realtor" style="background: linear-gradient(180deg, #3a4050 0%, var(--portrait-tone) 100%); border-radius: 60px 60px 0 0;"></div>

  <div class="intro">
    <h1 class="headline">PROPERTY FOR SALE</h1>
    <p class="presenting">Presenting</p>
    <p class="address">48207 Velmora Lane, Brandywine, MD</p>
    <p class="priced">Priced to Sell</p>
    <p class="price">Only $550,000</p>
    <p class="call">Call Today: (240) 555-0183</p>
    <p class="agent">Marcus Pelley, <small>Realtor</small></p>
    <p class="brokerage">Dunmore Realty Inc.</p>
    <p class="email">premierhomedesk@quillmail.example</p>
  </div>

  <div class="brand">DUNMORE REALTY INC.</div>
  <div class="badge" aria-hidden="true"></div>

  <div class="details">
    <h2 class="details__title">PROPERTY DETAILS</h2>
    <div class="details__cols">
      <ul class="details__list">
        <li><svg viewBox="0 0 10 10"><path d="M1 5.5 L4 8.5 L9 1.5" stroke="#fff" stroke-width="1.8" fill="none"/></svg>5 Bedroom / 4 Bathroom Colonial with Contemporary Design and Charm</li>
        <li><svg viewBox="0 0 10 10"><path d="M1 5.5 L4 8.5 L9 1.5" stroke="#fff" stroke-width="1.8" fill="none"/></svg>Over 5,000 sq ft of Spacious Elegance</li>
        <li><svg viewBox="0 0 10 10"><path d="M1 5.5 L4 8.5 L9 1.5" stroke="#fff" stroke-width="1.8" fill="none"/></svg>Modern Open Concept Kitchen</li>
        <li><svg viewBox="0 0 10 10"><path d="M1 5.5 L4 8.5 L9 1.5" stroke="#fff" stroke-width="1.8" fill="none"/></svg>Natural Oak Floors</li>
        <li><svg viewBox="0 0 10 10"><path d="M1 5.5 L4 8.5 L9 1.5" stroke="#fff" stroke-width="1.8" fill="none"/></svg>Stainless Steel Appliances</li>
      </ul>
      <ul class="details__list">
        <li><svg viewBox="0 0 10 10"><path d="M1 5.5 L4 8.5 L9 1.5" stroke="#fff" stroke-width="1.8" fill="none"/></svg>Extraordinary Master Bedroom with Spacious Bath</li>
        <li><svg viewBox="0 0 10 10"><path d="M1 5.5 L4 8.5 L9 1.5" stroke="#fff" stroke-width="1.8" fill="none"/></svg>Granite Counter-Tops</li>
        <li><svg viewBox="0 0 10 10"><path d="M1 5.5 L4 8.5 L9 1.5" stroke="#fff" stroke-width="1.8" fill="none"/></svg>Exterior with Outdoor Security, Design Lighting and Sprinkler System</li>
        <li><svg viewBox="0 0 10 10"><path d="M1 5.5 L4 8.5 L9 1.5" stroke="#fff" stroke-width="1.8" fill="none"/></svg>Just 10 Minutes From Corvel Landing</li>
      </ul>
    </div>
  </div>
</section>
</body>
</html>
```